Fashion Label Startup Business Card Design

Maribel Quint is a startup fashion designer based on the Gold Coast in QLD Australia. Maribels label " Vorine by Quint " is based upon taking old world design techniques and infusing them modern twist. The card design should incorporate an old world theme using colours like mustard, ocha, black, white and elements of lace pattern.

Card Details:

Maribel Quint
Fashion Designer
P: 04 0152 6847
E: vorinebyquint@mailbrook.com
W: www.friendsnet.com/VOrineByQuint

```html
<!DOCTYPE html>
<html lang="en">
<head>
<meta charset="utf-8">
<title>Vorine by Quint – Business Card</title>
<link rel="stylesheet" href="https://fonts.googleapis.com/css2?family=Gelasio:ital,wght@0,400;1,400&display=swap">
<style>
  :root {
    --page: #ecebe8;
    --card-cream: #f6f3ee;
    --card-sand: #e0d7c3;
    --sand-shadow: #d3c9b3;
    --mustard: #c9a24d;
    --ink: #3d3d41;
  }
  html, body {
    margin: 0;
    width: 1200px;
    height: 1000px;
    overflow: hidden;
    background: var(--page);
    font-family: "Gelasio", Georgia, serif;
  }
  .canvas { position: relative; width: 1200px; height: 1000px; }
  .card {
    position: absolute;
    top: 140px;
    width: 440px;
    height: 722px;
    background: var(--card-sand);
    overflow: hidden;
    box-shadow: 0 2px 6px rgba(0,0,0,0.12);
  }
  .card--front { left: 110px; }
  .card--back { left: 651px; }

  /* Front */
  .front-upper {
    position: absolute; left: 0; top: 0; width: 100%; height: 250px;
    background: var(--card-cream);
  }
  .lace-strip {
    position: absolute; left: 0; width: 100%; height: 24px;
    background: linear-gradient(to bottom, var(--card-cream), var(--sand-shadow));
  }
  .front-upper + .lace-strip { top: 238px; }
  .dress-form-art {
    position: absolute; left: 95px; top: 0; width: 250px; height: 700px;
    background: linear-gradient(to bottom, var(--mustard) 0%, var(--mustard) 47%, var(--sand-shadow) 62%, var(--card-sand) 100%);
    border-radius: 0 0 40px 40px;
    opacity: 0.9;
  }
  .brand-name {
    position: absolute; left: 0; right: 0; top: 395px;
    text-align: center;
    color: var(--ink);
    font-weight: 400;
    line-height: 0.95;
    margin: 0;
  }
  .brand-name .word { display: block; font-size: 70px; }
  .brand-name .joiner { display: block; font-size: 42px; }

  /* Back */
  .back-band {
    position: absolute; left: 0; width: 100%; height: 96px;
    background: var(--card-cream);
  }
  .back-band--top { top: 0; }
  .back-band--bottom { bottom: 0; }
  .lace-border {
    position: absolute; left: 0; width: 100%; height: 44px;
    background: var(--mustard);
    opacity: 0.75;
  }
  .back-band--top .lace-border { top: 40px; }
  .back-band--bottom .lace-border { top: 4px; }

  .holder-name {
    position: absolute; left: 29px; top: 128px; margin: 0;
    font-size: 88px; font-weight: 400; line-height: 95px;
    color: var(--ink);
  }
  .holder-role {
    position: absolute; left: 30px; top: 354px; margin: 0;
    font-size: 43px; font-style: italic; font-weight: 400;
    color: var(--mustard);
  }
  .contact-list {
    position: absolute; left: 31px; top: 464px;
    list-style: none; margin: 0; padding: 0;
  }
  .contact-item {
    display: flex; align-items: center;
    height: 47px;
    font-size: 20px; font-style: italic;
    color: var(--ink);
  }
  .contact-icon { width: 28px; height: 28px; margin-right: 14px; flex: none; }
</style>
</head>
<body>
<main class="canvas">

  <section class="card card--front" aria-label="Card front">
    <div class="front-upper"></div>
    <div class="lace-strip" role="img" aria-label="Lace trim pattern"></div>
    <div class="dress-form-art" role="img" aria-label="Illustration of a mustard dressmaker's form on a stand with pale forms behind"></div>
    <h1 class="brand-name">
      <span class="word">Vorine</span>
      <span class="joiner">by</span>
      <span class="word">Quint</span>
    </h1>
  </section>

  <section class="card card--back" aria-label="Card back">
    <div class="back-band back-band--top">
      <div class="lace-border" role="img" aria-label="Gold lace scroll border"></div>
    </div>

    <h2 class="holder-name">Maribel<br>Quint</h2>
    <p class="holder-role">Fashion Designer</p>

    <ul class="contact-list">
      <li class="contact-item">
        <svg class="contact-icon" viewBox="0 0 28 28" aria-hidden="true">
          <circle cx="14" cy="14" r="14" fill="var(--ink)"/>
          <path d="M7 12 Q14 6 21 12 L19 14 L16 12 L12 12 L9 14 Z" fill="var(--card-sand)"/>
          <rect x="10" y="14" width="8" height="6" rx="2" fill="var(--card-sand)"/>
        </svg>
        04 0152 6847
      </li>
      <li class="contact-item">
        <svg class="contact-icon" viewBox="0 0 28 28" aria-hidden="true">
          <circle cx="14" cy="14" r="14" fill="var(--ink)"/>
          <rect x="7" y="9" width="14" height="10" fill="none" stroke="var(--card-sand)" stroke-width="1.6"/>
          <path d="M7 9 L14 15 L21 9" fill="none" stroke="var(--card-sand)" stroke-width="1.6"/>
        </svg>
        vorinebyquint@mailbrook.com
      </li>
      <li class="contact-item">
        <svg class="contact-icon" viewBox="0 0 28 28" aria-hidden="true">
          <circle cx="14" cy="14" r="14" fill="var(--ink)"/>
          <path d="M12 7 h2.5 v6 h1.5 v-2 h2 v2 h1.5 v8 a2 2 0 0 1 -2 2 h-4 a3 3 0 0 1 -3 -3 v-4 h1.5 Z" fill="var(--card-sand)"/>
        </svg>
        www.friendsnet.com/VOrineByQuint
      </li>
    </ul>

    <div class="back-band back-band--bottom">
      <div class="lace-border" role="img" aria-label="Gold lace scroll border"></div>
    </div>
  </section>

</main>
</body>
</html>
```